Business Card Design Project

I require a business card for a new coaching business based in Melbourne with global clients. Both companies and individuals will retain our coaching services.

Target Market(s)

Both small business and large corporate in western speaking countries. Individuals requiring support and direction on issues such as fears, phobias, career, relationships, confidence, self esteem etc.

Industry/Entity Type

Business

Font styles to use
Sans Serif

Colors

Designer to choose colors to be used in the design.

Requirements
Must have
• White background to enhance the colours in the logo. Logo on the left.
Should not have
• The black and white version of the logo. Keep the colours.

```html
<!DOCTYPE html>
<html lang="en">
<head>
<meta charset="utf-8">
<title>Clear Path Coaching – Business Card</title>
<link rel="stylesheet" href="https://fonts.googleapis.com/css2?family=Roboto+Condensed:wght@400;700&family=Open+Sans:wght@400;600&display=swap">
<style>
  :root {
    --stage: #e9e6e1;
    --card: #ffffff;
    --card-shade: #eeeeee;
    --ink: #454545;
    --ink-soft: #5c5c5c;
    --accent: #f26a0f;
    --rule: #8a8a8a;
  }
  * { box-sizing: border-box; margin: 0; padding: 0; }
  html, body { width: 1200px; height: 1024px; overflow: hidden; }
  body {
    background: var(--stage);
    font-family: "Open Sans", sans-serif;
    color: var(--ink);
    position: relative;
  }
  .card {
    position: absolute;
    left: 250px;
    width: 700px;
    height: 400px;
    background: linear-gradient(135deg, var(--card) 55%, var(--card-shade));
    box-shadow: 0 8px 24px rgba(0,0,0,.18);
    overflow: hidden;
  }
  .card--front { top: 84px; }
  .card--back { top: 540px; }

  /* Wordmark */
  .wordmark {
    display: flex;
    align-items: center;
    gap: 16px;
  }
  .wordmark__dot {
    width: 34px; height: 34px;
    border-radius: 50%;
    background: var(--accent);
    flex: none;
  }
  .wordmark__name {
    font-family: "Roboto Condensed", sans-serif;
    font-weight: 700;
    color: var(--ink);
    text-transform: uppercase;
    line-height: .9;
    letter-spacing: -.5px;
  }

  /* Front */
  .front__brand {
    position: absolute;
    left: 0; top: 0;
    width: 270px; height: 100%;
    border-right: 1px solid #d6d6d6;
    padding: 0 0 0 34px;
    display: flex; align-items: center;
  }
  .front__brand .wordmark__name { font-size: 40px; }
  .front__abn {
    position: absolute;
    left: 34px; bottom: 30px;
    font-size: 15px;
    color: var(--ink);
    letter-spacing: .5px;
  }
  .front__details {
    position: absolute;
    left: 310px; top: 110px; right: 0;
  }
  .person__row { display: flex; align-items: center; gap: 12px; }
  .person__name {
    font-family: "Roboto Condensed", sans-serif;
    font-size: 28px;
    color: var(--accent);
    white-space: nowrap;
  }
  .person__row::after {
    content: "";
    flex: 1;
    height: 1px;
    background: var(--rule);
    margin-top: 8px;
  }
  .person__role { font-size: 14px; color: var(--ink-soft); margin-top: 4px; }
  .contact { list-style: none; margin-top: 34px; }
  .contact li {
    display: flex; align-items: center; gap: 12px;
    font-size: 15px; color: var(--ink-soft);
    margin-bottom: 16px;
  }
  .contact svg { width: 16px; height: 16px; fill: var(--accent); flex: none; }

  /* Back */
  .back__band {
    position: absolute; left: 0; right: 0;
    height: 72px;
    background: var(--accent);
    color: #fff;
    font-family: "Roboto Condensed", sans-serif;
    font-size: 24px;
    letter-spacing: 1px;
    text-transform: uppercase;
    display: flex; align-items: center; justify-content: center;
  }
  .back__band--top { top: 0; }
  .back__band--bottom { bottom: 0; }
  .back__brand {
    position: absolute; left: 0; right: 0; top: 72px; bottom: 72px;
    display: flex; align-items: center; justify-content: center;
  }
  .back__brand .wordmark__name { font-size: 54px; }
</style>
</head>
<body>
  <section class="card card--front" aria-label="Business card front">
    <div class="front__brand">
      <div class="wordmark">
        <span class="wordmark__dot"></span>
        <span class="wordmark__name">Clear Path<br>Coaching</span>
      </div>
    </div>
    <p class="front__abn">ABN&nbsp; 51824753556</p>
    <div class="front__details">
      <div class="person__row"><h1 class="person__name">Maren Holloway-Price</h1></div>
      <p class="person__role">Performance Consultant and Coach</p>
      <ul class="contact">
        <li>
          <svg viewBox="0 0 24 24" aria-hidden="true"><path d="M6.6 10.8a15.1 15.1 0 0 0 6.6 6.6l2.2-2.2a1 1 0 0 1 1-.25 11.4 11.4 0 0 0 3.6.57 1 1 0 0 1 1 1V20a1 1 0 0 1-1 1A17 17 0 0 1 3 4a1 1 0 0 1 1-1h3.5a1 1 0 0 1 1 1c0 1.25.2 2.45.57 3.57a1 1 0 0 1-.25 1z"/></svg>
          +61 (0) 400 555 019
        </li>
        <li>
          <svg viewBox="0 0 24 24" aria-hidden="true"><path d="M3 5h18a1 1 0 0 1 1 1v12a1 1 0 0 1-1 1H3a1 1 0 0 1-1-1V6a1 1 0 0 1 1-1zm9 7 8-5H4z"/></svg>
          maren.coach@example.com
        </li>
      </ul>
    </div>
  </section>

  <section class="card card--back" aria-label="Business card back">
    <p class="back__band back__band--top">The mind is more powerful than the body</p>
    <div class="back__brand">
      <div class="wordmark">
        <span class="wordmark__dot"></span>
        <span class="wordmark__name">Clear Path<br>Coaching</span>
      </div>
    </div>
    <p class="back__band back__band--bottom">Give yourself permission to shine</p>
  </section>
</body>
</html>
```